Food and Beverage Business Cards

We need business cards with logo designs for a consultant in the food and beverage industry. We specialize in helping restaurants fix operational and management problems.
Specific areas of expertise include:
-Steps of service
-Staff management tools
-Standard operating procedures
-Profit and loss management
-Inventory
-Point of sales
-Bar Menu
-Mystery shopper service
-Handling and managing suppliers

Target Market(s)

Restaurant and bar owners and managers

Industry/Entity Type

Business

Contact Information for Business Card

Mathieu Delorme
K&T Consulting
phone: 15027390618
mathkt@brindlemail.net

Font styles to use
Other font styles liked:
• Check out the screen shot font idea

Colors

Designer to choose colors to be used in the design.

Requirements
Must have
• Must include QR code (See attachment)
• Logo should reflect our specific focus on the drinks side of the industry.
• Areas of Expertise:
• -Service Steps
• -Staff management tools
• -S.O.P
• -P&L Management
• -Inventory
• -P.O.S
• -Bar Menu
• -Mystery Shopper Service
• -Handling and Managing Suppliers

```html
<!DOCTYPE html>
<html lang="en">
<head>
<meta charset="utf-8">
<title>K&amp;T Consulting Business Cards</title>
<link href="https://fonts.googleapis.com/css2?family=Source+Sans+3:wght@400;600;700&display=swap" rel="stylesheet">
<style>
  :root {
    --backdrop: #5b4a3a;
    --card-white: #f3f3f3;
    --card-black: #151414;
    --ink: #111111;
    --ink-soft: #4a4a4a;
    --paper-text: #ffffff;
    --badge-ring: #dcdcdc;
  }
  * { margin: 0; padding: 0; box-sizing: border-box; }
  html, body { width: 1200px; height: 960px; overflow: hidden; }
  body {
    background: var(--backdrop);
    font-family: "Source Sans 3", "Myriad Pro", Arial, sans-serif;
    position: relative;
  }
  .card {
    position: absolute;
    width: 600px;
    height: 343px;
    overflow: hidden;
  }
  .card-front { left: 314px; top: 113px; background: var(--card-white); }
  .card-back { left: 311px; top: 472px; background: var(--card-black); color: var(--paper-text); }

  .front-swoosh { position: absolute; inset: 0; }

  .brand-name {
    position: absolute;
    font-weight: 700;
    white-space: nowrap;
    letter-spacing: 0.5px;
  }
  .card-front .brand-name { left: 24px; top: 62px; font-size: 38px; color: var(--ink); }

  .contact {
    position: absolute;
    right: 33px;
    top: 220px;
    text-align: right;
  }
  .contact-name { font-size: 20px; font-weight: 700; color: var(--ink); letter-spacing: 0.2px; }
  .contact-company { font-size: 15px; color: var(--ink-soft); letter-spacing: 0.5px; margin-top: 2px; }
  .contact-lines { margin-top: 20px; font-size: 15px; color: var(--ink); line-height: 19px; }
  .contact-line { display: flex; justify-content: flex-end; align-items: center; gap: 7px; }
  .contact-line svg { width: 14px; height: 12px; flex: none; }

  .badges { position: absolute; right: 20px; top: 16px; display: flex; gap: 6px; }
  .badge {
    width: 48px; height: 48px; border-radius: 50%;
    background: var(--paper-text);
    border: 3px solid var(--badge-ring);
    box-shadow: inset 0 0 0 4px var(--card-black);
  }

  .card-back .brand-name {
    left: 0; right: 0; top: 100px;
    text-align: center;
    font-size: 54px;
    color: var(--paper-text);
  }
  .expertise { position: absolute; left: 0; right: 0; top: 222px; text-align: center; }
  .expertise-title { font-size: 21px; font-weight: 600; margin-bottom: 4px; }
  .expertise-list { font-size: 15.5px; line-height: 20px; }
</style>
</head>
<body>
  <section class="card card-front">
    <svg class="front-swoosh" viewBox="0 0 600 343" width="600" height="343" aria-hidden="true">
      <path d="M330 0 C 470 20 570 80 600 150 L600 0 Z" fill="var(--card-black)"/>
      <path d="M330 0 C 470 20 570 80 600 150" fill="none" stroke="#bdbdbd" stroke-width="3"/>
      <path d="M355 4 C 480 25 565 80 598 128" fill="none" stroke="#ffffff" stroke-width="2" opacity="0.8"/>
      <path d="M0 192 C 30 270 170 330 290 343 L0 343 Z" fill="var(--card-black)"/>
      <path d="M0 192 C 30 270 170 330 290 343" fill="none" stroke="#bdbdbd" stroke-width="3"/>
      <path d="M8 222 C 60 290 180 330 270 342" fill="none" stroke="#ffffff" stroke-width="2" opacity="0.8"/>
    </svg>
    <div class="brand-name">K&amp;T Midtown</div>
    <div class="contact">
      <div class="contact-name">MATHIEU DELORME</div>
      <div class="contact-company">K&amp;T CONSULTING</div>
      <div class="contact-lines">
        <div class="contact-line">15027390618
          <svg viewBox="0 0 14 12" aria-hidden="true"><path d="M1 4 Q7 0 13 4 L11 6 L9 4.5 L5 4.5 L3 6 Z M3 7 L11 7 L12 11 L2 11 Z" fill="var(--ink)"/></svg>
        </div>
        <div class="contact-line">mathkt@brindlemail.net
          <svg viewBox="0 0 14 12" aria-hidden="true"><rect x="1" y="2" width="12" height="8" fill="var(--ink)"/><path d="M1 2 L7 7 L13 2" fill="none" stroke="#ffffff" stroke-width="1"/></svg>
        </div>
      </div>
    </div>
  </section>

  <section class="card card-back">
    <div class="badges">
      <div class="badge"></div>
      <div class="badge"></div>
    </div>
    <div class="brand-name">K&amp;T Midtown</div>
    <div class="expertise">
      <div class="expertise-title">Areas of Expertise</div>
      <div class="expertise-list">
        Service Steps | Staff management tools | S.O.P | P&amp;L Management<br>
        Inventory | P.O.S | Bar Menu | Mystery Shopper Service<br>
        Handling and Managing Suppliers
      </div>
    </div>
  </section>
</body>
</html>
```